Business card design needed for Automotive Reconditioning business

I have a logo design i just cant decide on the best color or layout for the business card, I will upload all the files so you can see all colors schemes we are considering. I have other file formats if needed let me know.

Target Market(s)

automotive dealerships

Contact Information for Business Card

HERE are the Descriptions and info needed on the card:
Interior Repair: Leather carpet burns panels dash Deoderize
Dealer products and Vin Verify
( spot for name and cell number) My name is Norman Bexley phone 614 352-4180 Title COO www.QuorvalMotive.com

Font styles to use
Sans Serif
Other font styles liked:
• what ever you think looks best

Requirements
Must have
• Must be able to change the name and phone for employees

```html
<!DOCTYPE html>
<html lang="en">
<head>
<meta charset="utf-8">
<title>Quorval Motive Business Card</title>
<link href="https://fonts.googleapis.com/css2?family=Montserrat:wght@300;400;600;700;800&display=swap" rel="stylesheet">
<style>
  :root {
    --page: #e9eaeb;
    --card: #2b2b2d;
    --card-deep: #1f1f21;
    --check-light: #f2f2f2;
    --check-dark: #161616;
    --red: #d2402f;
    --red-deep: #b8301f;
    --blue: #4a86c8;
    --text: #ffffff;
    --text-soft: #d8d8d8;
  }
  * { margin: 0; padding: 0; box-sizing: border-box; }
  html, body { width: 1200px; height: 969px; overflow: hidden; }
  body {
    background: var(--page);
    font-family: "Montserrat", sans-serif;
    position: relative;
  }
  .card {
    position: absolute;
    width: 540px;
    height: 309px;
    border-radius: 6px;
    overflow: hidden;
    box-shadow: 0 8px 24px rgba(0,0,0,0.18);
  }
  /* Front */
  .card--front { left: 330px; top: 120px; background: var(--card); }
  .front__flag {
    position: absolute; left: 0; top: 0; width: 180px; height: 100%;
    background: linear-gradient(115deg, var(--check-light) 0%, #9a9a9a 45%, var(--check-dark) 75%, var(--card) 100%);
    clip-path: polygon(0 0, 55% 0, 90% 100%, 0 100%);
  }
  .front__brand {
    position: absolute; left: 168px; top: 64px;
    white-space: nowrap;
  }
  .front__name {
    color: var(--red);
    font-size: 30px; font-weight: 800; letter-spacing: 1px; line-height: 1;
  }
  .front__tagline {
    display: inline-block; margin-top: 8px;
    background: var(--blue); color: var(--text);
    font-size: 14px; font-weight: 700; letter-spacing: 0.5px;
    padding: 4px 10px;
  }
  .service {
    position: absolute; display: flex; align-items: center; gap: 12px;
    color: var(--text-soft); font-size: 13px; line-height: 1.35;
    white-space: nowrap;
  }
  .service__icon {
    width: 40px; height: 40px; border-radius: 6px; background: var(--red);
    flex-shrink: 0; display: flex; align-items: center; justify-content: center;
  }
  .service--interior { left: 168px; bottom: 32px; }
  .service--dealer { right: 32px; top: 160px; }
  .service__title { font-weight: 700; color: var(--text); }
  /* Back */
  .card--back { left: 330px; top: 520px; background: var(--card-deep); }
  .back__pattern {
    position: absolute; inset: 0;
    background: radial-gradient(ellipse at 45% 40%, #4a4a4c 0%, #333335 50%, #222224 100%);
  }
  .back__nameplate {
    position: absolute; left: 70px; top: 92px;
    background: linear-gradient(180deg, var(--red) 0%, var(--red-deep) 100%);
    border-radius: 10px; padding: 14px 26px;
    color: var(--text); font-size: 34px; letter-spacing: 1px;
    white-space: nowrap;
  }
  .back__first { font-weight: 700; }
  .back__last { font-weight: 300; }
  .back__title {
    position: absolute; left: 318px; top: 160px;
    background: var(--blue); color: var(--text);
    font-size: 20px; font-weight: 300; letter-spacing: 1px;
    padding: 4px 22px; border-radius: 0 0 8px 8px;
  }
  .back__phone {
    position: absolute; left: 80px; top: 228px;
    display: flex; align-items: center; gap: 12px;
    color: var(--text); font-size: 26px; font-weight: 400; letter-spacing: 1px;
  }
</style>
</head>
<body>
  <section class="card card--front">
    <div class="front__flag" role="img" aria-label="Checkered racing flag pattern"></div>
    <div class="front__brand">
      <div class="front__name">QUORVAL MOTIVE</div>
      <div class="front__tagline">AUTO RECONDITIONING CORP.</div>
    </div>
    <div class="service service--dealer">
      <div class="service__icon">
        <svg width="24" height="24" viewBox="0 0 24 24" fill="none" stroke="#fff" stroke-width="2" stroke-linecap="round">
          <path d="M6 5v14M18 5v14M6 12h12"/>
        </svg>
      </div>
      <div>Dealer products &amp;<br>Vin Verify</div>
    </div>
    <div class="service service--interior">
      <div class="service__icon">
        <svg width="24" height="24" viewBox="0 0 24 24" fill="none" stroke="#fff" stroke-width="1.8" stroke-linejoin="round">
          <rect x="4" y="4" width="6" height="10" rx="2"/><rect x="14" y="4" width="6" height="10" rx="2"/>
          <path d="M3 14h8v5H3zM13 14h8v5h-8z"/>
        </svg>
      </div>
      <div>
        <div class="service__title">Interior Repair:</div>
        <div>Leather Carpet Burns</div>
        <div>Panels Dash Deoderize</div>
      </div>
    </div>
  </section>

  <section class="card card--back">
    <div class="back__pattern" role="img" aria-label="Faint waving checkered flag pattern"></div>
    <div class="back__title">COO</div>
    <div class="back__nameplate"><span class="back__first">NORMAN</span><span class="back__last">BEXLEY</span></div>
    <div class="back__phone">
      <svg width="30" height="30" viewBox="0 0 30 30" fill="none" stroke="#fff" stroke-width="2">
        <circle cx="15" cy="15" r="13"/>
        <path d="M10 8.5l3 3-1.8 1.8a8 8 0 0 0 5.5 5.5L18.5 17l3 3-2 2c-5.5 0-11.5-6-11.5-11.5z" stroke-linejoin="round"/>
      </svg>
      <span>614 352-4180</span>
    </div>
  </section>
</body>
</html>
```